Visit card for Luxury Alpine home

Cedar Brook Chalet (Hinterthal, Austria) – visit card

Brief: To design a visit card (4/4) that can be both left for existing guests and handed out to friends/business contacts to promote our luxury holiday home in the Austrian alps which can be rented year -round but primarily for summer (hiking/biking/golf) and winter (skiing). Primary focus is for family as its a 3br/3ba place that is usually booked for either a larger family or two families.

Basic information required/purpose: email/contact info. Basic information about the place, location, possibly some ideas/icons about what to do. Imagery that gives people the idea about luxury/fun/mountains etc. Hopefully the card would be something to interest them enough to check out the website and eventually make a direct booking with us.

Our details and photos:

https://cedarbrookchalet.com
https://www.friendwall.net/cedarbrookchalet/

contact information for people to book:
stay.cedarbrook@postvale.com
+420 612408953

some other resources:

http://www.valdoriska.at/en/vacation.html
the moutains are called Hochkoenig and our village is Hinterthal which is next to Maria alm

Target Market(s)

European (winter) and Middle-Eastern (summer) families.

Industry/Entity Type

Travel

Contact Information for Business Card

standard 4/4 to be used for prospect

Font styles to use
Sans Serif

Colors

Designer to choose colors to be used in the design.

Requirements
Must have
• all relevant information for the client to contact us
• colorful/luxury imagery of the property (we can provide better photo quality that the web downloads)
Nice to have
• not particular about fonts. preferring subdued colours

```html
<!DOCTYPE html>
<html lang="en">
<head>
<meta charset="utf-8">
<title>Cedar Brook Chalet – Visit Card</title>
<link href="https://fonts.googleapis.com/css2?family=Bebas+Neue&family=Open+Sans:wght@400;600&display=swap" rel="stylesheet">
<style>
  :root {
    --page: #e8e9eb;
    --wine: #a91d3a;
    --gold: #fdc314;
    --ink: #1c1c1c;
    --white: #ffffff;
    --sky: #7fb0d3;
    --frost: #e9eef2;
  }
  * { margin: 0; padding: 0; box-sizing: border-box; }
  html, body { width: 1200px; height: 1000px; overflow: hidden; background: var(--page); }
  body { position: relative; font-family: "Open Sans", Arial, sans-serif; }

  .card {
    position: absolute; top: 276px; width: 416px; height: 415px; overflow: hidden;
    box-shadow: 10px 12px 22px rgba(0,0,0,0.18);
  }
  .card--front { left: 176px; background: var(--white); }
  .card--back { left: 636px; background: var(--wine); }

  .display { font-family: "Bebas Neue", Impact, sans-serif; line-height: 0.8; position: absolute; white-space: nowrap; }

  /* front: header */
  .header-band { position: absolute; left: 94px; top: 0; width: 322px; height: 132px; background: var(--wine); }
  .brand-badge {
    position: absolute; left: 29px; top: 0; width: 132px; height: 132px; border-radius: 50%;
    background: var(--white); border: 8px solid var(--wine);
    display: flex; align-items: center; justify-content: center; text-align: center;
  }
  .brand-name { font-family: "Bebas Neue", Impact, sans-serif; font-size: 31px; line-height: 0.9; color: var(--ink); }
  .tagline { left: 210px; top: 34px; color: var(--white); display: flex; align-items: flex-end; }
  .tagline-small { font-size: 40px; line-height: 0.85; }
  .tagline-big { font-size: 88px; line-height: 0.8; margin-left: 2px; margin-bottom: -4px; }

  /* front: photos */
  .photo { position: absolute; top: 136px; height: 137px; }
  .photo--bedroom { left: 0; width: 203px; background: linear-gradient(160deg, #5a4d47 0%, #7a2530 55%, #e6e1dc 100%); }
  .photo--lounge { left: 205px; width: 211px; background: linear-gradient(160deg, #d9cbb8 0%, #8a7460 55%, #5a4a3c 100%); }

  /* front: booking */
  .booking-band {
    position: absolute; left: 0; top: 275px; width: 380px; height: 140px;
    background: var(--gold); border-radius: 0 70px 70px 0;
  }
  .booking-title { left: 15px; top: 303px; font-size: 44px; color: var(--ink); }
  .contact { position: absolute; left: 16px; display: flex; align-items: center; gap: 8px; font-size: 12px; color: var(--ink); }
  .contact--phone { top: 352px; }
  .contact--mail { top: 378px; }
  .contact-icon { width: 22px; height: 22px; border-radius: 50%; background: var(--ink); display: flex; align-items: center; justify-content: center; }
  .photo--suite {
    position: absolute; left: 250px; top: 282px; width: 126px; height: 126px; border-radius: 50%;
    background: linear-gradient(170deg, #6d5f58 0%, #3b2f3d 50%, #efece8 100%);
  }

  /* back */
  .web { transform: rotate(-90deg); transform-origin: left top; }
  .web-prefix { left: 46px; top: 348px; font-size: 30px; color: var(--gold); }
  .web-name { left: 70px; top: 350px; font-size: 48px; color: var(--white); }
  .web-suffix { left: 122px; top: 100px; font-size: 22px; color: var(--gold); }

  .word { color: transparent; -webkit-background-clip: text; background-clip: text; }
  .word--tracking { left: 164px; top: 56px; font-size: 32px; background-image: linear-gradient(var(--sky), var(--sky)); }
  .word--summer { left: 164px; top: 86px; font-size: 58px; background-image: linear-gradient(180deg, #cfe2ef, #7fb0d3 70%, #e9eef2); }
  .word--golfing { left: 228px; top: 136px; font-size: 36px; background-image: linear-gradient(180deg, #ffffff, #d9dfe3); }
  .word--australian { left: 164px; top: 170px; font-size: 55px; background-image: linear-gradient(180deg, #ffffff, #c9d0d6 60%, #8a8f92); }
  .word--alps { left: 300px; top: 214px; font-size: 42px; background-image: linear-gradient(180deg, #ffffff, #e3e7ea); }
  .word--skiing { left: 164px; top: 243px; font-size: 44px; background-image: linear-gradient(180deg, #ffffff, #cfd5da); }
  .word--winter { left: 164px; top: 284px; font-size: 88px; background-image: linear-gradient(180deg, #d8dde0 0%, #5c5552 45%, #2c2a28 100%); }
  .word--biking { left: 328px; top: 162px; font-size: 52px; transform: rotate(-90deg); transform-origin: left top; background-image: linear-gradient(90deg, #ffffff, #d8dee2); }

  .rule { position: absolute; background: var(--white); height: 8px; }
  .rule--a { left: 272px; top: 67px; width: 46px; }
  .rule--b { left: 166px; top: 146px; width: 56px; }
  .rule--c { left: 166px; top: 224px; width: 128px; }
  .rule--d { left: 266px; top: 261px; width: 103px; }
</style>
</head>
<body>

<section class="card card--front" aria-label="Front of visit card">
  <div class="header-band"></div>
  <div class="brand-badge"><span class="brand-name">Cedar<br>Brook<br>Chalet</span></div>
  <div class="display tagline">
    <span class="tagline-small">Stay<br>With</span><span class="tagline-big">Us</span>
  </div>

  <div class="photo photo--bedroom" role="img" aria-label="Photo of the chalet bedroom with twin beds and a red headboard"></div>
  <div class="photo photo--lounge" role="img" aria-label="Photo of the chalet living room with sofa, coffee table and TV"></div>

  <div class="booking-band"></div>
  <div class="display booking-title">For Booking</div>
  <div class="contact contact--phone">
    <span class="contact-icon">
      <svg width="8" height="12" viewBox="0 0 8 12"><rect x="0.75" y="0.75" width="6.5" height="10.5" rx="1.2" fill="none" stroke="#fdc314" stroke-width="1.5"/><circle cx="4" cy="9.3" r="0.8" fill="#fdc314"/></svg>
    </span>
    <span>+42 061 240 8953</span>
  </div>
  <div class="contact contact--mail">
    <span class="contact-icon">
      <svg width="12" height="9" viewBox="0 0 12 9"><rect x="0" y="0" width="12" height="9" rx="1" fill="#fdc314"/><path d="M0.5 0.8 L6 5 L11.5 0.8" fill="none" stroke="#1c1c1c" stroke-width="1.2"/></svg>
    </span>
    <span>stay.cedarbrook@postvale.com</span>
  </div>
  <div class="photo--suite" role="img" aria-label="Round photo of a guest bedroom with twin beds"></div>
</section>

<section class="card card--back" aria-label="Back of visit card">
  <div class="display web web-prefix">www.</div>
  <div class="display web web-name">CedarBrookChalet</div>
  <div class="display web web-suffix">.com</div>

  <div class="display word word--tracking">Tracking</div>
  <div class="rule rule--a"></div>
  <div class="display word word--summer">Summer</div>
  <div class="rule rule--b"></div>
  <div class="display word word--golfing">Golfing</div>
  <div class="display word word--biking">Biking</div>
  <div class="display word word--australian">Australian</div>
  <div class="rule rule--c"></div>
  <div class="display word word--alps">Alps</div>
  <div class="display word word--skiing">Skiing</div>
  <div class="rule rule--d"></div>
  <div class="display word word--winter">Winter</div>
</section>

</body>
</html>
```